The Corran & Wexby Irish Bar Bendigo

I need an app for my local hotel/pub. We have a bistro, functions and live entertainment every week. I would like to promote meal deals, drink offers, upcoming shows, members benefits. I would need to be able to update daily. Thanks
Updates

Reason: I am away on holidays until 19th July and can only get contact rarely so follow up is only on my phone not computer. Thanks Gordon

Target Market(s)

18+

Industry/Entity Type

Entertainment

Requirements
Must have
• Promotions
Entertainment
Functions
About the hotel

```html
<!DOCTYPE html>
<html lang="en">
<head>
<meta charset="utf-8">
<title>The Corran &amp; Wexby – App Screens</title>
<link href="https://fonts.googleapis.com/css2?family=Arvo:wght@400;700&family=Arimo:ital,wght@0,400;0,700;1,400&display=swap" rel="stylesheet">
<style>
  :root{
    --stage:#1f7f3c;
    --bar:#000;
    --header-top:#3a3a3a;
    --header-bottom:#151515;
    --brand-green:#6fc43a;
    --panel-top:#9a9a9a;
    --panel-bottom:#5e5e5e;
    --row-top:#e4f3d4;
    --row-bottom:#b9dc9f;
    --row-edge:#8fb878;
    --drink:#c0321c;
    --meal:#2f8f2a;
    --band:#1d5fd0;
    --member:#c98200;
    --badge-red:#d9361c;
    --badge-green:#2f9a2f;
    --badge-blue:#1d6fe0;
    --badge-amber:#d08a10;
    --orange:#e26b12;
    --icon-red:#d9664a;
    --ink:#111;
    --price:#c4180c;
    --white:#fff;
  }
  *{box-sizing:border-box;margin:0;padding:0}
  html,body{width:1200px;height:650px;overflow:hidden}
  body{background:var(--stage);font-family:"Arimo",Arial,sans-serif;position:relative}

  .screen{position:absolute;top:131px;width:238px;height:357px;overflow:hidden;background:linear-gradient(var(--panel-top),var(--panel-bottom))}
  .screen--home{left:143px}
  .screen--list{left:539px}
  .screen--detail{left:852px}

  .status{height:16px;background:var(--bar);color:#ddd;font-size:9.5px;font-weight:700;display:flex;align-items:center;padding:0 6px;position:relative}
  .status .carrier{margin-left:3px}
  .status .net{margin-left:6px}
  .status .time{position:absolute;left:0;right:0;text-align:center;font-size:10px}
  .status .battery{margin-left:auto;width:14px;height:7px;border:1px solid #ccc;padding:1px}
  .status .battery i{display:block;height:100%;background:#ccc}
  .signal{display:flex;gap:1px;align-items:flex-end;height:7px}
  .signal i{width:2px;background:#ddd}

  .app-header{height:56px;background:linear-gradient(var(--header-top),var(--header-bottom));display:flex;align-items:center;padding-left:16px;gap:10px}
  .brand-mark{width:36px;height:36px;background:var(--brand-green);border-radius:3px}
  .brand-name{font-family:"Arvo",Georgia,serif;color:var(--brand-green);font-size:12.5px;line-height:1;text-transform:uppercase}
  .brand-sub{color:#eee;font-size:9.5px;margin-top:2px}

  .section-title{font-family:"Arvo",Georgia,serif;font-weight:700;color:#fff;font-size:11.5px;position:absolute;left:10px;top:81px}

  .row{position:absolute;left:10px;width:218px;height:40px;border-radius:3px;background:linear-gradient(var(--row-top),var(--row-bottom));border:1px solid var(--row-edge);box-shadow:0 1px 1px rgba(0,0,0,.35)}
  .cat-icon{position:absolute;left:3px;top:3px;width:32px;height:32px;border-radius:2px;display:flex;align-items:center;justify-content:center}
  .cat-label{position:absolute;left:42px;top:12px;font-family:"Arvo",Georgia,serif;font-weight:700;font-size:11.5px}
  .total{position:absolute;right:7px;top:13px;height:13px;width:52px;border-radius:7px;background:#c9d2be;border:1px solid #9aa590;font-size:7.5px;font-weight:700;line-height:11px;padding-left:5px;color:#333}
  .total b{position:absolute;right:-1px;top:-1px;height:13px;width:20px;border-radius:7px;color:#fff;text-align:center;line-height:13px;font-size:7.5px}

  .btn{position:absolute;top:277px;height:41px;border-radius:3px;display:flex;align-items:center;font-family:"Arvo",Georgia,serif;font-weight:700;font-size:11.5px;line-height:1;box-shadow:0 1px 1px rgba(0,0,0,.35)}
  .btn--info{left:10px;width:106px;background:linear-gradient(#7fbf62,#3e8a2c);color:#fff;padding-left:8px;gap:12px}
  .btn--functions{left:121px;width:107px;background:linear-gradient(#f39a3c,#d45f0c);color:#5a2a00;padding-left:8px;gap:8px}

  .footer{position:absolute;left:0;right:0;bottom:0;height:29px;background:#2a2a2a;display:flex;align-items:center;justify-content:center}
  .stamp{display:flex;font-size:6.5px;font-weight:700;border-radius:6px;overflow:hidden}
  .stamp span{background:#bbb;color:#333;padding:2px 5px}
  .stamp time{background:#555;color:#eee;padding:2px 5px}

  .titlebar{position:absolute;left:2px;right:2px;top:80px;height:24px;background:linear-gradient(#d6d6d6,#9c9c9c);border-radius:2px}
  .back{position:absolute;left:0;top:0;height:24px;width:44px;background:var(--orange);color:#fff;font-size:7px;font-weight:700;display:flex;align-items:center;justify-content:center;clip-path:polygon(8px 0,100% 0,100% 100%,8px 100%,0 50%)}
  .titlebar h1{font-family:"Arvo",Georgia,serif;font-size:12px;text-align:center;line-height:24px;color:#222}
  .titlebar .count{position:absolute;right:8px;top:5px;width:20px;height:14px;border-radius:7px;background:var(--badge-red);color:#fff;font-size:8px;font-weight:700;text-align:center;line-height:14px}

  .offer{position:absolute;left:10px;width:218px;height:40px;border-radius:3px;background:linear-gradient(var(--row-top),var(--row-bottom));border:1px solid var(--row-edge)}
  .offer .cat-icon{background:var(--icon-red);border:1px solid #a03a22}
  .offer h2{position:absolute;left:42px;top:4px;font-size:11px;font-weight:700;line-height:12px;color:var(--ink);width:150px}
  .offer .from{position:absolute;left:42px;bottom:4px;font-size:6.5px;font-weight:700;color:var(--price)}
  .offer .dates{position:absolute;left:113px;bottom:4px;font-size:6.5px;font-style:italic;color:var(--price)}
  .offer .chev{position:absolute;right:6px;top:13px;width:0;height:0;border-left:9px solid #555;border-top:7px solid transparent;border-bottom:7px solid transparent}

  .offer--open{height:127px;background:var(--white);border-color:#ddd}
  .offer--open .from,.offer--open .dates{top:30px;bottom:auto}
  .offer--open .toggle{position:absolute;right:7px;top:17px;border-top:8px solid var(--price);border-left:6px solid transparent;border-right:6px solid transparent}
  .offer-photo{position:absolute;left:5px;top:42px;width:101px;height:80px;background:linear-gradient(135deg,#5a8a2e,#d04a3a 45%,#3a6ab0 75%,#1d2a18)}
  .offer-text{position:absolute;left:114px;top:44px;width:100px;font-size:7px;line-height:9.5px;color:#222}
</style>
</head>
<body>

<svg width="0" height="0" style="position:absolute">
  <defs>
    <symbol id="glass" viewBox="0 0 24 24"><path d="M4 5h16l-7 8v6h4v2H7v-2h4v-6z" fill="none" stroke="#fff" stroke-width="1.8" stroke-linejoin="round"/><circle cx="17" cy="5" r="3" fill="none" stroke="#fff" stroke-width="1.5"/></symbol>
  </defs>
</svg>

<!-- Home screen -->
<section class="screen screen--home">
  <div class="status"><span class="signal"><i style="height:2px"></i><i style="height:3px"></i><i style="height:5px"></i><i style="height:7px"></i></span><span class="carrier">KESTREL</span><span class="net">3G</span><span class="time">4:20 PM</span><span class="battery"><i></i></span></div>
  <header class="app-header"><div class="brand-mark"></div><div><div class="brand-name">The Corran &amp; Wexby</div><div class="brand-sub">Irish Bar - Bendigo</div></div></header>
  <h2 class="section-title">WHAT'S ON</h2>

  <div class="row" style="top:103px"><span class="cat-icon" style="background:var(--icon-red)"><svg width="20" height="20"><use href="#glass"/></svg></span><span class="cat-label" style="color:var(--drink)">Drink Offers</span><span class="total">Total<b style="background:var(--badge-red)">15</b></span></div>
  <div class="row" style="top:147px"><span class="cat-icon" style="background:#3fa03a"><svg width="20" height="20" viewBox="0 0 24 24"><path d="M5 3l14 16M19 3L5 19" stroke="#fff" stroke-width="2.2" stroke-linecap="round"/></svg></span><span class="cat-label" style="color:var(--meal)">Meal Deals</span><span class="total">Total<b style="background:var(--badge-green)">3</b></span></div>
  <div class="row" style="top:190px"><span class="cat-icon" style="background:#2d6fd6"><svg width="22" height="20" viewBox="0 0 24 22"><circle cx="6" cy="9" r="2.5" fill="#fff"/><circle cx="12" cy="9" r="2.5" fill="#fff"/><circle cx="18" cy="9" r="2.5" fill="#fff"/><path d="M2 19q4-7 8 0M8 19q4-7 8 0M14 19q4-7 8 0" fill="#fff"/><path d="M3 4h18" stroke="#fff" stroke-width="1.5"/></svg></span><span class="cat-label" style="color:var(--band)">Bands &amp; Shows</span><span class="total">Total<b style="background:var(--badge-blue)">10</b></span></div>
  <div class="row" style="top:234px"><span class="cat-icon" style="background:#e0a018"><svg width="24" height="24" viewBox="0 0 24 24"><path d="M9 2l2 5h5l-4 3 1.5 5L9 12l-4.5 3L6 10 2 7h5z" fill="#7a3f00"/><path d="M17 13l1.2 3h3l-2.4 1.8.9 3-2.7-1.8-2.7 1.8.9-3-2.4-1.8h3z" fill="#7a3f00"/></svg></span><span class="cat-label" style="color:var(--member)">Member Offers</span><span class="total">Total<b style="background:var(--badge-amber)">2</b></span></div>

  <div class="btn btn--info"><svg width="16" height="16" viewBox="0 0 16 16"><circle cx="8" cy="8" r="7.5" fill="#fff"/><rect x="7" y="7" width="2" height="6" fill="#3e8a2c"/><circle cx="8" cy="4.5" r="1.2" fill="#3e8a2c"/></svg><span>Hotel<br>Info</span></div>
  <div class="btn btn--functions"><svg width="22" height="20" viewBox="0 0 22 20"><path d="M3 2v17" stroke="#7a3a00" stroke-width="1.6"/><path d="M3 3q5-3 9 0t8 0v8q-4 3-8 0t-9 0z" fill="#b84a00"/></svg><span>Functions</span></div>

  <footer class="footer"><div class="stamp"><span>Last update</span><time>12/07/2012</time></div></footer>
</section>

<!-- Drink offers list -->
<section class="screen screen--list">
  <div class="status"><span class="signal"><i style="height:2px"></i><i style="height:3px"></i><i style="height:5px"></i><i style="height:7px"></i></span><span class="carrier">KESTREL</span><span class="net">3G</span><span class="time">4:20 PM</span><span class="battery"><i></i></span></div>
  <header class="app-header"><div class="brand-mark"></div><div><div class="brand-name">The Corran &amp; Wexby</div><div class="brand-sub">Irish Bar - Bendigo</div></div></header>
  <div class="titlebar"><span class="back">Menu</span><h1>Drink Offers</h1><span class="count">15</span></div>

  <article class="offer" style="top:111px"><span class="cat-icon"><svg width="20" height="20"><use href="#glass"/></svg></span><h2>Non-alkoholic cocktails</h2><span class="from">FROM $9.90</span><span class="dates">01/07/2012-01/10/2012</span><span class="chev"></span></article>
  <article class="offer" style="top:155px"><span class="cat-icon"><svg width="20" height="20"><use href="#glass"/></svg></span><h2>Healthy Juice</h2><span class="from">FROM $1.90</span><span class="dates">01/07/2012-01/10/2012</span><span class="chev"></span></article>
  <article class="offer" style="top:198px"><span class="cat-icon"><svg width="20" height="20"><use href="#glass"/></svg></span><h2>Healthy Juice</h2><span class="from">FROM $1.90</span><span class="dates">01/07/2012-01/10/2012</span><span class="chev"></span></article>
  <article class="offer" style="top:242px"><span class="cat-icon"><svg width="20" height="20"><use href="#glass"/></svg></span><h2>Healthy Juice</h2><span class="from">FROM $1.90</span><span class="dates">01/07/2012-01/10/2012</span><span class="chev"></span></article>
  <article class="offer" style="top:285px"><span class="cat-icon"><svg width="20" height="20"><use href="#glass"/></svg></span><h2>Lorem ipsum dolor sit amet headline text</h2><span class="from">FROM $1.90</span><span class="dates">01/07/2012-01/10/2012</span><span class="chev"></span></article>
  <article class="offer" style="top:329px"><span class="cat-icon"><svg width="20" height="20"><use href="#glass"/></svg></span><h2>Lorem ipsum dolor sit amet headline text</h2><span class="from">FROM $1.90</span><span class="dates">01/07/2012-01/10/2012</span><span class="chev"></span></article>
</section>

<!-- Drink offers with expanded item -->
<section class="screen screen--detail">
  <div class="status"><span class="signal"><i style="height:2px"></i><i style="height:3px"></i><i style="height:5px"></i><i style="height:7px"></i></span><span class="carrier">KESTREL</span><span class="net">3G</span><span class="time">4:20 PM</span><span class="battery"><i></i></span></div>
  <header class="app-header"><div class="brand-mark"></div><div><div class="brand-name">The Corran &amp; Wexby</div><div class="brand-sub">Irish Bar - Bendigo</div></div></header>
  <div class="titlebar"><span class="back">Menu</span><h1>Drink Offers</h1><span class="count">15</span></div>

  <article class="offer offer--open" style="top:111px"><span class="cat-icon"><svg width="20" height="20"><use href="#glass"/></svg></span><h2>Non-alkoholic cocktails</h2><span class="from">FROM $9.90</span><span class="dates">01/07/2012-01/10/2012</span><span class="toggle"></span>
    <div class="offer-photo" role="img" aria-label="Photo of colourful cocktails in glasses"></div>
    <p class="offer-text">Lorem ipsum dolor sit amet, consectetur adipiscing elit. Nunc tempus ante in nulla posuere tristique ultricies sapien semper.<br>• anyname: $4<br>• anyname: $4</p>
  </article>
  <article class="offer" style="top:242px"><span class="cat-icon"><svg width="20" height="20"><use href="#glass"/></svg></span><h2>Healthy Juice</h2><span class="from">FROM $1.90</span><span class="dates">01/07/2012-01/10/2012</span><span class="chev"></span></article>
  <article class="offer" style="top:285px"><span class="cat-icon"><svg width="20" height="20"><use href="#glass"/></svg></span><h2>Lorem ipsum dolor sit amet headline text</h2><span class="from">FROM $1.90</span><span class="dates">01/07/2012-01/10/2012</span><span class="chev"></span></article>
  <article class="offer" style="top:329px"><span class="cat-icon"><svg width="20" height="20"><use href="#glass"/></svg></span><h2>Lorem ipsum dolor sit amet headline text</h2><span class="from">FROM $1.90</span><span class="dates">01/07/2012-01/10/2012</span><span class="chev"></span></article>
</section>

</body>
</html>
```